Boutique Fitness Facility needs a new meal plan design that is as hot as our workouts!

We are about to host our 6 week Heatwave Reset program and we need to have a great looking meal plan handout created that we can give to all of our participants.

I have attached an example of our current full meal plan, for a reference only.

As in the example I've provided, I'd like to have certain areas color coded such as the proteins being Blue, Fats -yellow, Carbs - orange and veggies- green.

These colors will corollate to the Breakfast - snack - lunch - snack - Dinner graph that I've provided and would like to have added to the new handout.

I would like our logo placed at the top and beneath the logo have the text "Heatwave Reset Challenge"

The flyer should be of a summer influence in colors and design and
All text should be easy to read.

Thank you and I look forward to seeing your design!

```html
<!DOCTYPE html>
<html lang="en">
<head>
<meta charset="utf-8">
<title>Heatwave Reset Challenge – Meal Plan</title>
<link rel="stylesheet" href="https://fonts.googleapis.com/css2?family=Lilita+One&family=Poppins:wght@400;500;600;700;800&display=swap">
<style>
  :root{
    --blue:#3b4bb0;
    --yellow:#f6d10f;
    --orange:#f39220;
    --green:#4cb848;
    --green-text:#3aa935;
    --cream:#fbf9ee;
    --ink:#0e0e0e;
    --white:#ffffff;
    --stage:#adadad;
  }
  *{box-sizing:border-box;margin:0;padding:0}
  html,body{width:1200px;height:1200px;overflow:hidden;background:var(--stage)}
  body{position:relative;font-family:"Poppins",sans-serif}
  .flyer{position:absolute;left:136px;top:0;width:928px;height:1200px;overflow:hidden;background:var(--ink)}
  .gym-backdrop{position:absolute;left:0;top:0;width:928px;height:730px;
    background:radial-gradient(ellipse at 55% 40%,#3a3a3a 0%,#1e1e1e 45%,#0b0b0b 100%)}
  .abs{position:absolute}

  .brand-name{left:62px;top:62px;width:334px;font-weight:800;font-size:55px;line-height:1;color:var(--white);letter-spacing:-1px}
  .brand-divider{left:426px;top:54px;width:1px;height:102px;background:#6a6a6a}
  .title-main{left:458px;top:42px;font-family:"Lilita One",sans-serif;font-size:78px;line-height:1;color:var(--yellow);letter-spacing:1px}
  .title-sub{left:460px;top:116px;font-family:"Lilita One",sans-serif;font-size:45px;line-height:1;color:var(--white);letter-spacing:.5px}

  .food-group{position:absolute;top:184px;width:176px;height:368px}
  .food-group svg{position:absolute;left:0;top:0}
  .group-label{position:absolute;top:5px;left:0;width:176px;text-align:center;font-weight:700;font-size:17px;color:var(--white)}
  .group-fats .group-label,.group-carbs .group-label{color:var(--ink)}
  .food-list{position:absolute;left:10px;top:53px;list-style:none;width:162px}
  .food-list li{position:relative;padding-left:25px;font-size:11.2px;font-weight:500;line-height:13.5px;color:var(--white);margin-bottom:10.5px}
  .food-list li::before{content:"";position:absolute;left:4px;top:1px;width:12px;height:12px;border-radius:50%;background:var(--dot)}
  .group-protein{left:63px;--dot:var(--blue)}
  .group-fats{left:273px;--dot:var(--yellow)}
  .group-carbs{left:481px;--dot:var(--orange)}
  .group-veg{left:700px;--dot:var(--green)}

  .note-tag{left:62px;top:581px;width:97px;height:33px;background:var(--white);border-radius:8px;font-weight:700;font-size:18px;line-height:33px;text-align:center;color:var(--ink)}
  .note-text{left:185px;top:582px;font-size:20.5px;color:var(--white);white-space:nowrap;line-height:30px}
  .note-text .chev{color:var(--yellow);font-weight:600;margin-right:6px}
  .note-text .gap{display:inline-block;width:22px}

  .cream-panel{position:absolute;left:0;top:0}

  .meal{position:absolute;top:633px;width:160px;height:160px}
  .meal svg{position:absolute;left:0;top:0}
  .meal-name{position:absolute;left:0;width:160px;text-align:center;top:90px;font-weight:700;font-size:14px;color:var(--white);letter-spacing:.3px}
  .meal-art{position:absolute;left:64px;top:52px;width:32px;height:30px;border-radius:6px;background:var(--yellow);opacity:.85}
  .meal-breakfast{left:58px}
  .meal-lunch{left:381px}
  .meal-dinner{left:714px}

  .snack{position:absolute;width:120px;height:120px}
  .snack svg{position:absolute;left:0;top:0}
  .snack-portion{position:absolute;left:0;top:88px;width:120px;text-align:center;font-weight:700;font-size:11px;line-height:14px;color:var(--ink)}
  .snack-one{left:238px;top:672px}
  .snack-two{left:572px;top:672px}

  .fuel-head{left:61px;top:838px;font-family:"Lilita One",sans-serif;line-height:1}
  .fuel-head .line-a{display:block;font-size:39px;color:var(--ink);letter-spacing:.5px}
  .fuel-head .line-b{display:block;font-size:22px;color:#e2bd0a;margin-top:1px;letter-spacing:.3px}
  .fuel-band{position:absolute;left:0;top:0}
  .fuel-copy{left:340px;top:840px;font-size:15.4px;line-height:19.5px;color:var(--ink);font-weight:400}

  .tip{position:absolute;top:932px}
  .tip-art{width:56px;height:56px;border-radius:6px;background:#1b1b1b}
  .tip-title{margin-top:10px;font-weight:700;font-size:17.5px;line-height:21.5px;color:var(--green-text)}
  .tip-body{margin-top:10px;font-size:10.3px;line-height:12.6px;color:var(--ink)}
  .tip-1{left:62px}.tip-2{left:211px}.tip-3{left:394px}.tip-4{left:572px}.tip-5{left:736px}
  .tip-rule{position:absolute;top:930px;width:1px;height:230px;background:linear-gradient(#e9e6d6,rgba(233,230,214,0))}
</style>
</head>
<body>
<main class="flyer">
  <div class="gym-backdrop" role="img" aria-label="Dark photo of a gym with weight racks and benches"></div>

  <header>
    <div class="abs brand-name">PulseForge</div>
    <div class="abs brand-divider"></div>
    <h1>
      <span class="abs title-main">HEATWAVE</span>
      <span class="abs title-sub">RESET CHALLENGE</span>
    </h1>
  </header>

  <!-- food groups -->
  <section class="food-group group-protein">
    <svg width="176" height="368" viewBox="0 0 176 368">
      <path d="M1 11 V367 H136 L175 328 V11" fill="none" stroke="var(--blue)" stroke-width="1.5"/>
      <polygon points="14,0 141,0 155,30 28,30" fill="var(--blue)"/>
    </svg>
    <div class="group-label">PROTEIN</div>
    <ul class="food-list">
      <li>1 - 1 1/2 scoop protein<br>powder</li>
      <li>4-6 oz Chicken Breast</li>
      <li>4-6oz Turkey Breast</li>
      <li>4-6 oz Filet Mignon</li>
      <li>4-6 oz Flank Steak</li>
      <li>4-6 oz Salmon</li>
      <li>4-6 oz Tuna</li>
      <li>4-6 oz Cod</li>
      <li>4-6 oz Cottage Cheese</li>
      <li>4-6 oz Greek Yogurt</li>
      <li>4-6 oz Tofu</li>
      <li>3 -5 egg whites + 1<br>whole egg</li>
    </ul>
  </section>

  <section class="food-group group-fats">
    <svg width="176" height="368" viewBox="0 0 176 368">
      <path d="M1 11 V367 H136 L175 328 V11" fill="none" stroke="var(--yellow)" stroke-width="1.5"/>
      <polygon points="14,0 141,0 155,30 28,30" fill="var(--yellow)"/>
    </svg>
    <div class="group-label">FATS</div>
    <ul class="food-list">
      <li>¼ - ½ Avocado</li>
      <li>1 tbs Olive Oil</li>
      <li>1 small handful<br>Almonds, Walnuts,<br>Cashews</li>
      <li>1 tbs Greenhollow<br>Grass Fed Butter</li>
    </ul>
  </section>

  <section class="food-group group-carbs">
    <svg width="176" height="368" viewBox="0 0 176 368">
      <path d="M1 11 V367 H136 L175 328 V11" fill="none" stroke="var(--orange)" stroke-width="1.5"/>
      <polygon points="14,0 141,0 155,30 28,30" fill="var(--orange)"/>
    </svg>
    <div class="group-label">CARBS</div>
    <ul class="food-list">
      <li>3 – 4oz Sweet Potato</li>
      <li>¼ - ½ cup White Rice</li>
      <li>¼ - ½ cup Quinoa</li>
      <li>¼ - ½ cup Oatmeal</li>
      <li>¾ cup Blueberries</li>
      <li>¾ cup Strawberries</li>
      <li>¾ cup Raspberries</li>
      <li>1 med. Apple</li>
      <li>1 small orange</li>
      <li>1 small grapefruit</li>
    </ul>
  </section>

  <section class="food-group group-veg">
    <svg width="176" height="368" viewBox="0 0 176 368">
      <path d="M1 11 V367 H136 L175 328 V11" fill="none" stroke="var(--green)" stroke-width="1.5"/>
      <polygon points="14,0 141,0 155,30 28,30" fill="var(--green)"/>
    </svg>
    <div class="group-label">VEGETABLES</div>
    <ul class="food-list">
      <li>1 Scoop Powdered<br>Greens</li>
      <li>1 Cup Sautéed<br>Spinach</li>
      <li>1 Cup Sautéed Kale,<br>Broccoli</li>
      <li>1 Cup Sautéed Bell<br>Pepper</li>
      <li>1 Cup Sautéed Carrots</li>
      <li>1 Cup Sautéed<br>Zucchini</li>
    </ul>
  </section>

  <div class="abs note-tag">NOTE:</div>
  <p class="abs note-text"><span class="chev">&lt;</span>150 lbs stick to smaller portions<span class="gap"></span><span class="chev">&gt;</span>150 lbs stick to larger portions.</p>

  <!-- cream lower panel with torn edge -->
  <svg class="cream-panel" width="928" height="1200" viewBox="0 0 928 1200">
    <polygon fill="var(--cream)" points="0,712 40,708 75,714 120,705 170,713 215,706 260,715 300,709 350,716 400,707 450,714 500,706 545,715 590,708 640,714 690,705 735,713 780,707 830,715 880,706 928,712 928,1200 0,1200"/>
  </svg>

  <!-- meal flow -->
  <div class="meal meal-breakfast">
    <svg width="160" height="160" viewBox="-80 -80 160 160">
      <circle r="68" fill="none" stroke="var(--blue)" stroke-width="19" stroke-dasharray="134 400" transform="rotate(-78)"/>
      <circle r="68" fill="none" stroke="var(--green)" stroke-width="19" stroke-dasharray="134 400" transform="rotate(42)"/>
      <circle r="68" fill="none" stroke="var(--orange)" stroke-width="19" stroke-dasharray="134 400" transform="rotate(162)"/>
      <circle r="59" fill="var(--ink)"/>
      <g font-family="Poppins,sans-serif" font-size="8" font-weight="700" text-anchor="middle">
        <circle cx="-51" cy="-25" r="8" fill="var(--white)"/><text x="-51" y="-22" fill="var(--ink)">1</text>
        <circle cx="51" cy="-26" r="8" fill="var(--white)"/><text x="51" y="-23" fill="var(--ink)">1</text>
        <circle cx="0" cy="60" r="8" fill="var(--white)"/><text x="0" y="63" fill="var(--ink)">1</text>
      </g>
    </svg>
    <div class="meal-art" role="img" aria-label="Breakfast food icon"></div>
    <div class="meal-name" style="top:88px">BREAKFAST</div>
  </div>

  <div class="snack snack-one">
    <svg width="120" height="120" viewBox="0 0 120 120">
      <path d="M10 16 Q30 0 52 16" fill="none" stroke="var(--yellow)" stroke-width="5" stroke-linecap="round"/>
      <polygon points="47,8 60,20 44,24" fill="var(--yellow)"/>
      <path d="M66 16 Q86 0 108 16" fill="none" stroke="var(--white)" stroke-width="5" stroke-linecap="round"/>
      <polygon points="103,8 116,20 100,24" fill="var(--white)"/>
      <polygon points="2,37 14,37 14,63 2,63" fill="#2f7d2b"/>
      <polygon points="106,37 118,37 118,63 106,63" fill="#2f7d2b"/>
      <polygon points="12,36 108,36 100,64 20,64" fill="var(--green)"/>
      <text x="60" y="57" text-anchor="middle" font-family="Poppins,sans-serif" font-weight="700" font-size="14" fill="var(--white)">SNACK</text>
    </svg>
    <div class="snack-portion">1/2 PORTION<br>OF PROTEIN</div>
  </div>

  <div class="meal meal-lunch">
    <svg width="160" height="160" viewBox="-80 -80 160 160">
      <circle r="68" fill="none" stroke="var(--blue)" stroke-width="19" stroke-dasharray="134 400" transform="rotate(-78)"/>
      <circle r="68" fill="none" stroke="var(--green)" stroke-width="19" stroke-dasharray="134 400" transform="rotate(42)"/>
      <circle r="68" fill="none" stroke="var(--orange)" stroke-width="19" stroke-dasharray="134 400" transform="rotate(162)"/>
      <circle r="59" fill="var(--ink)"/>
      <g font-family="Poppins,sans-serif" font-size="8" font-weight="700" text-anchor="middle">
        <circle cx="-51" cy="-25" r="8" fill="var(--white)"/><text x="-51" y="-22" fill="var(--ink)">1</text>
        <circle cx="51" cy="-26" r="8" fill="var(--white)"/><text x="51" y="-23" fill="var(--ink)">1</text>
        <circle cx="0" cy="60" r="8" fill="var(--white)"/><text x="0" y="63" fill="var(--ink)">1</text>
      </g>
    </svg>
    <div class="meal-art" role="img" aria-label="Lunch plate icon" style="top:48px"></div>
    <div class="meal-name" style="top:92px">LUNCH</div>
  </div>

  <div class="snack snack-two">
    <svg width="120" height="120" viewBox="0 0 120 120">
      <path d="M10 16 Q30 0 52 16" fill="none" stroke="var(--yellow)" stroke-width="5" stroke-linecap="round"/>
      <polygon points="47,8 60,20 44,24" fill="var(--yellow)"/>
      <path d="M66 16 Q86 0 108 16" fill="none" stroke="var(--white)" stroke-width="5" stroke-linecap="round"/>
      <polygon points="103,8 116,20 100,24" fill="var(--white)"/>
      <polygon points="2,37 14,37 14,63 2,63" fill="#2f7d2b"/>
      <polygon points="106,37 118,37 118,63 106,63" fill="#2f7d2b"/>
      <polygon points="12,36 108,36 100,64 20,64" fill="var(--green)"/>
      <text x="60" y="57" text-anchor="middle" font-family="Poppins,sans-serif" font-weight="700" font-size="14" fill="var(--white)">SNACK</text>
    </svg>
    <div class="snack-portion">1/2 PORTION<br>OF PROTEIN</div>
  </div>

  <div class="meal meal-dinner">
    <svg width="160" height="160" viewBox="-80 -80 160 160">
      <circle r="68" fill="none" stroke="var(--blue)" stroke-width="19" stroke-dasharray="134 400" transform="rotate(-78)"/>
      <circle r="68" fill="none" stroke="var(--green)" stroke-width="19" stroke-dasharray="134 400" transform="rotate(42)"/>
      <circle r="68" fill="none" stroke="var(--yellow)" stroke-width="19" stroke-dasharray="134 400" transform="rotate(162)"/>
      <circle r="59" fill="var(--ink)"/>
      <g font-family="Poppins,sans-serif" font-size="8" font-weight="700" text-anchor="middle">
        <circle cx="-51" cy="-25" r="8" fill="var(--white)"/><text x="-51" y="-22" fill="var(--ink)">1</text>
        <circle cx="51" cy="-26" r="8" fill="var(--white)"/><text x="51" y="-23" fill="var(--ink)">1</text>
        <circle cx="0" cy="60" r="8" fill="var(--white)"/><text x="0" y="63" fill="var(--ink)">1</text>
      </g>
    </svg>
    <div class="meal-art" role="img" aria-label="Dinner roast icon" style="top:48px"></div>
    <div class="meal-name" style="top:92px">DINNER</div>
  </div>

  <!-- fuel section -->
  <svg class="fuel-band" width="928" height="1200" viewBox="0 0 928 1200">
    <polygon fill="var(--yellow)" points="305,822 340,818 380,824 430,817 480,823 540,816 600,824 660,818 720,823 780,816 840,822 900,817 928,820 928,917 880,921 820,914 760,920 700,913 640,919 580,914 520,921 460,915 400,920 350,914 310,918 308,880 303,850"/>
  </svg>
  <h2 class="abs fuel-head"><span class="line-a">FUEL YOUR</span><span class="line-b">HEATWAVE RESET!</span></h2>
  <p class="abs fuel-copy">This plan isn't about starving yourself - it's about sculpting a lean,<br>toned physique by shredding fat while preserving muscle.<br>Here's how to maximize your results</p>

  <div class="tip-rule" style="left:190px"></div>
  <div class="tip-rule" style="left:366px"></div>
  <div class="tip-rule" style="left:543px"></div>
  <div class="tip-rule" style="left:713px"></div>

  <article class="tip tip-1">
    <div class="tip-art" role="img" aria-label="Pictogram of a person eating at a table"></div>
    <h3 class="tip-title">Eat Like a<br>Champion</h3>
    <p class="tip-body">Stick to this list<br>as close as<br>possible for<br>maximum<br>results, 7 Days<br>A Week.</p>
  </article>
  <article class="tip tip-2">
    <div class="tip-art" role="img" aria-label="Pictogram of a running person"></div>
    <h3 class="tip-title">Burn More Than<br>You Consume</h3>
    <p class="tip-body">This is the golden<br>rule! You need to<br>burn more calories<br>than you consume<br>to create a deficit<br>and force your body<br>to tap into fat stores<br>for energy.</p>
  </article>
  <article class="tip tip-3">
    <div class="tip-art" role="img" aria-label="Pictogram of a person sleeping in bed"></div>
    <h3 class="tip-title">Maximize<br>Sleep</h3>
    <p class="tip-body">When sleep-deprived,<br>your body produces<br>more ghrelin (hunger<br>hormone) and less<br>leptin (satiety<br>hormone). Aim for<br>7-8 hours of quality<br>sleep nightly.</p>
  </article>
  <article class="tip tip-4">
    <div class="tip-art" role="img" aria-label="Icon of protein foods: fish, shaker and egg"></div>
    <h3 class="tip-title">Prioritize<br>Protein</h3>
    <p class="tip-body">Protein helps build<br>and maintain<br>muscle mass,<br>which is crucial for<br>boosting<br>metabolism and<br>burning more<br>calories at rest.</p>
  </article>
  <article class="tip tip-5">
    <div class="tip-art" role="img" aria-label="Crown icon"></div>
    <h3 class="tip-title">Consistency is<br>King/Queen</h3>
    <p class="tip-body">Don't expect overnight<br>results. Stick to your<br>plan, track your<br>progress, and<br>celebrate small<br>victories. Remember,<br>slow and steady wins<br>the shred race!</p>
  </article>
</main>
</body>
</html>
```